'The Lindqvist Draft' needs a movie poster

We need a movie poster for our short film coming up.

Genre: Drama/Mystery

Plot/Synopsis:
The Lindqvist Draft explores the fraught relationship between creation and destiny, the creator and the created: inspiration, obsession, destruction.
In the opening scene we are introduced to Walter Lindqvist and a young writer, Nora, whose stories play out decades apart and yet are intricately linked. Walter struggles with a block during the writing of his first novel; Nora, obsessed with uncovering her own past is inexplicably drawn to Lindqvist’s house and accepts a room for let from Greta, a strange woman who also resides there. As the two woman avoid delving too deep into each other’s pasts, suspicious of their intentions, Nora discovers that Walter mysteriously died without finishing his debut novel and Greta is most certainly holding something back.
Tensions are raised as Nora settles into Walter’s office and investigates the chattels left behind on his bureau. Accidentally marking a waiting page of manuscript, she unlocks a sixth sense of déjà vu, obsession seeps into possession and the voice of the author comes to life in an unexpected manner in order to enact his long awaited epilogue. With-in the novel, Nora finds the key to her past and confronts Greta with what she uncovers.
Dealing with the dark and destructive side of creativity, The Lindqvist Draft is an edgy mystery with a lurking subtext; Or is it just the greatest plot twist penned by a non-living author.

I have attached for you some images taken from the video camera.
Feel free to add any graphic if you want. I don't have a particular idea of how I want the poster so far so you are pretty free as long as The poster is appealing to the public and make them want to see the film and is related to the synopsis.

-An MoVantReel Production see our logo attached in the pictures
-Director by Tomaso Ruffini
-screenplay by Danny Wolcott

-Staring: (by order of importance)
Marthe Quillon
Lorna Brisbee
Glen Mabbott
Rolf Dunning

-Log line: Are you here to fill those pages?

Feel free to use any of those pictures or any of your design if you have ideas. Or even combine some of our pics with some design of yours.
Nora the lead actress is the young girl on the picture. she has to be in the poster. The other older woman is Greta! She is the supporting role-an important key of the story but very mysterious. (she doesn’t have to be in the poster)

Also it is IMPORTANT for me to have this poster in a format that I can edit as I will need to add some more names in the crew & music credit. Important that you could make the changes for me too include in this price.

Target Market(s)

Film festivals

Industry/Entity Type

Movie

Colors

Designer to choose colors to be used in the design.

Requirements
Must have
• The lead Nora (the young girl) in the poster.
• The producer logo must appear.
• A good title writing style.
• Drama feel.
Nice to have
• It would be nice to incorporate a gun in the design of the title 'The Lindqvist Draft'

```html
<!DOCTYPE html>
<html lang="en">
<head>
<meta charset="utf-8">
<title>The Lindqvist Draft — Poster</title>
<link rel="stylesheet" href="https://fonts.googleapis.com/css2?family=Courier+Prime:wght@400;700&family=Shadows+Into+Light&display=swap">
<style>
  :root {
    --paper: #d7d1c7;
    --paper-light: #e2ddd4;
    --paper-edge: #efebe3;
    --ink: #2b2a28;
    --sky-teal: #7fb3ba;
    --sky-mauve: #8a7378;
    --wash-red: #b8444a;
    --wash-deep: #8f3338;
  }
  html, body {
    margin: 0;
    padding: 0;
    overflow: hidden;
    background: #ffffff;
  }
  .poster {
    position: relative;
    width: 812px;
    height: 1200px;
    overflow: hidden;
    background: var(--paper);
  }
  .poster__art {
    position: absolute;
    inset: 0;
    display: block;
  }
  .tagline {
    position: absolute;
    left: 43px;
    top: 72px;
    margin: 0;
    font-family: "Courier Prime", monospace;
    font-weight: 700;
    font-size: 15.5px;
    color: var(--ink);
  }
  .title {
    position: absolute;
    left: 0;
    top: 0;
    margin: 0;
    font-family: "Shadows Into Light", cursive;
    font-weight: 400;
    color: var(--ink);
    line-height: 1;
  }
  .title__line {
    position: absolute;
    white-space: nowrap;
    letter-spacing: 0.16em;
  }
  .title__line--the { left: 296px; top: 286px; font-size: 72px; }
  .title__line--name { left: 86px; top: 396px; font-size: 84px; letter-spacing: 0.13em; }
  .title__line--draft { left: 228px; top: 514px; font-size: 80px; }
  .credits {
    position: absolute;
    left: 45px;
    top: 966px;
    font-family: "Courier Prime", monospace;
    color: var(--ink);
  }
  .credits__byline {
    margin: 0;
    font-weight: 700;
    font-size: 15.5px;
    line-height: 25px;
  }
  .credits__block {
    margin: 12px 0 0 0;
    font-weight: 700;
    font-size: 7.6px;
    line-height: 11px;
    text-transform: uppercase;
    letter-spacing: 0.02em;
  }
  .credits__block small {
    font-size: 5.6px;
    font-weight: 400;
  }
  .producer-mark {
    display: flex;
    align-items: center;
    gap: 3px;
    margin-top: 8px;
    font-family: "Courier Prime", monospace;
    font-weight: 700;
    font-size: 6px;
    color: var(--ink);
  }
  .producer-mark__square {
    width: 7px;
    height: 7px;
    background: var(--ink);
  }
</style>
</head>
<body>
  <main class="poster">
    <svg class="poster__art" width="812" height="1200" viewBox="0 0 812 1200" aria-hidden="false">
      <defs>
        <linearGradient id="photoWash" x1="0" y1="0" x2="0.2" y2="1">
          <stop offset="0" stop-color="#cfe4e6"/>
          <stop offset="0.08" stop-color="var(--sky-teal)"/>
          <stop offset="0.26" stop-color="var(--sky-mauve)"/>
          <stop offset="0.5" stop-color="var(--wash-red)"/>
          <stop offset="0.8" stop-color="var(--wash-deep)"/>
          <stop offset="1" stop-color="#9e5a58"/>
        </linearGradient>
        <radialGradient id="portraitShade" cx="0.5" cy="0.45" r="0.6">
          <stop offset="0" stop-color="#c86a66"/>
          <stop offset="1" stop-color="#8a3a3c" stop-opacity="0"/>
        </radialGradient>
        <linearGradient id="paperTone" x1="0" y1="0" x2="1" y2="1">
          <stop offset="0" stop-color="var(--paper-light)"/>
          <stop offset="1" stop-color="var(--paper)"/>
        </linearGradient>
      </defs>

      <g class="photo-panel" role="img" aria-label="Photograph: a young woman with long dark hair, half her face showing beside the torn page, under a teal-to-red cloudy sky">
        <rect x="0" y="0" width="812" height="1200" fill="url(#photoWash)"/>
        <ellipse cx="560" cy="800" rx="200" ry="380" fill="url(#portraitShade)"/>
      </g>

      <path class="torn-page__edge" fill="var(--paper-edge)"
        d="M0 0 L568 0 L563 40 L556 80 L546 120 L534 160 L520 210 L508 250 L494 290 L480 330 L468 370 L458 410 L452 450 L446 490 L440 530 L436 570 L430 620 L426 670 L424 720 L420 780 L418 840 L420 900 L424 960 L428 1020 L432 1080 L436 1140 L440 1200 L0 1200 Z"/>
      <path class="torn-page" fill="url(#paperTone)"
        d="M0 0 L562 0 L558 20 L553 45 L548 70 L542 98 L537 122 L529 150 L522 178 L514 210 L506 240 L497 268 L488 298 L478 330 L468 362 L460 392 L454 420 L450 448 L444 480 L440 512 L436 545 L432 578 L428 612 L425 645 L423 680 L421 716 L418 752 L416 790 L415 828 L416 866 L418 904 L421 942 L424 980 L427 1018 L430 1056 L432 1094 L434 1132 L436 1170 L437 1200 L0 1200 Z"/>
    </svg>

    <p class="tagline">Are you here to fill those pages?</p>

    <h1 class="title" aria-label="The Lindqvist Draft">
      <span class="title__line title__line--the">THE</span>
      <span class="title__line title__line--name">LINDQVIST</span>
      <span class="title__line title__line--draft">DRAFT</span>
    </h1>

    <section class="credits">
      <p class="credits__byline">a film by<br>Tomaso Ruffini</p>
      <p class="credits__block">
        <small>AN</small> MoVantReel <small>PRODUCTION</small> "THE LINDQVIST DRAFT"<br>
        <small>STARRING</small> MARTHE QUILLON&nbsp; LORNA BRISBEE&nbsp; GLEN MABBOTT<br>
        <small>AND</small> ROLF DUNNING&nbsp; <small>SCREENPLAY BY</small> DANNY WOLCOTT<br>
        <small>DIRECTED BY</small> TOMASO RUFFINI
      </p>
      <div class="producer-mark">
        <span class="producer-mark__square"></span>
        <span class="producer-mark__name">MoVantReel</span>
      </div>
    </section>
  </main>
</body>
</html>
```